Remove darkness and cobwebs from www.tovrelly.com

I need your help for my mission to do fun language teaching shows for English learners in Spain. This is a site for magic shows that teach English to Spanish kids.

The text will stay pretty much the same, but I would like to update it to a scrolling one pager, make it brighter- and make it more mobile friendly.

I have some added new photos as well. (Sadly the web page isn't the only thing getting older... but I like to tell myself that I am hiding it better than my page.)

Target Market(s)

Education, It is primarily seen by teachers - female, ages 25-40.

Industry/Entity Type

Education

Number of Pages Required

1 page

Font styles to use
Serif
Sans Serif
Decorative

Requirements
Must have
• Modified to a one page design, easy to make responsive.
• Floating navigation bar.
• Following sections:
• Welcome.
• University and EOI (Escuela Official de Idiomas)
• ESO & Bachillerato (High School)
• Primaria (Primary School)
• Infantíl (Very Young Learners)
• Meet the Artist
• Contact.
• Would like to include the following colors:
• E54430
• F6A51C
• 44B0A6
• 3695B5
Nice to have
• Parallax video backgrounds thought of in the design.
• Logo adapted to colors of page.
Should not have
• Pip the baker undertones... this has to go across the whole educational spectrum.

```html
<!DOCTYPE html>
<html lang="en">
<head>
<meta charset="utf-8">
<title>Tovrelly Productions</title>
<link href="https://fonts.googleapis.com/css2?family=Oswald:wght@400;500&family=Roboto:wght@400;500&display=swap" rel="stylesheet">
<style>
:root{
  --red:#e54430;
  --red-dark:#c7321f;
  --gold:#f6a51c;
  --teal:#44b0a6;
  --teal-dark:#3a9a8c;
  --blue:#3695b5;
  --blue-deep:#2e6e92;
  --ink:#222;
  --text:#444;
  --grey-bg:#ededed;
  --white:#fff;
  --bar:#1f1f1f;
}
*{box-sizing:border-box;margin:0;padding:0}
html,body{width:1200px;height:3416px;overflow:hidden}
body{font-family:'Roboto',Arial,sans-serif;color:var(--text);background:var(--white);position:relative}
section,header,footer,nav{position:absolute;left:0;width:1200px}
.abs{position:absolute}
.heading{font-family:'Oswald',Arial,sans-serif;font-weight:400;text-transform:uppercase;color:var(--ink);font-size:32px;letter-spacing:.3px}
.heading em{font-style:normal;color:var(--red)}
.centered{text-align:center;left:0;width:1200px}
.copy{font-size:13px;line-height:22px;color:#444}
.btn{position:absolute;display:flex;align-items:center;justify-content:center;font-size:15px;color:var(--white);border-radius:3px}

/* header */
.site-header{top:0;height:137px;background:var(--white)}
.phone{left:91px;top:54px;display:flex;align-items:center;gap:10px;font-size:22px;color:var(--ink);font-weight:500}
.brand{left:540px;top:40px;display:flex;align-items:center;gap:10px;font-family:'Oswald',Arial,sans-serif;font-weight:500;font-size:34px;color:var(--red)}
.brand .dot{width:22px;height:22px;border-radius:50%;background:var(--red)}
.quote-btn{left:963px;top:50px;width:148px;height:48px;background:linear-gradient(#f8b53a,#e4930e);font-family:'Oswald',Arial,sans-serif;font-size:17px;text-transform:uppercase;border:1px solid #d88a0c}

/* nav */
.main-nav{top:137px;height:66px;background:linear-gradient(var(--red),var(--red-dark))}
.main-nav ul{list-style:none;position:absolute;left:91px;top:0;height:66px;display:flex}
.main-nav li{height:66px;display:flex;align-items:center;padding:0 21px;color:var(--white);font-size:16px;text-transform:uppercase}
.main-nav li.active{background:#222;padding:0 30px}

/* hero */
.hero{top:203px;height:557px;background:radial-gradient(ellipse at 65% 40%,#4a4a4a 0%,#2a2a2a 55%,#151515 100%)}
.hero-photo{left:600px;top:0;width:600px;height:557px;background:radial-gradient(ellipse at 50% 45%,rgba(120,30,30,.35),rgba(0,0,0,0) 65%)}
.hero-title{left:109px;top:320px;font-family:'Oswald',Arial,sans-serif;font-size:44px;color:var(--white);text-transform:uppercase}
.hero-sub{left:109px;top:380px;font-family:'Oswald',Arial,sans-serif;font-size:29px;color:var(--white)}
.play{left:572px;top:224px}
.dots{left:1042px;top:516px;display:flex;gap:8px}
.dots span{width:12px;height:12px;border-radius:50%;background:var(--white)}
.dots span.on{background:var(--red);box-shadow:0 0 0 2px #fff}

/* welcome */
.welcome{top:760px;height:230px}
.welcome .heading{top:52px}
.welcome .copy{left:91px;top:110px;width:1020px;text-align:center}

/* university */
.university{top:990px;height:581px;background:var(--grey-bg)}
.university .heading{top:48px}
.card{position:absolute;top:210px;width:330px;height:305px;border-radius:6px;color:var(--white);text-align:center}
.card.teal{left:91px;background:var(--teal)}
.card.red{left:435px;background:var(--red)}
.card.blue{left:779px;background:var(--blue)}
.card .portrait{position:absolute;left:69px;top:-95px;width:192px;height:192px;border-radius:50%;border:6px solid var(--white);box-shadow:0 2px 6px rgba(0,0,0,.3)}
.card h3{position:absolute;left:0;width:100%;top:128px;font-family:'Oswald',Arial,sans-serif;font-weight:400;font-size:22px;text-transform:uppercase}
.card p{position:absolute;left:28px;width:274px;top:170px;font-size:12px;line-height:16px}
.card .more{position:absolute;left:0;width:100%;top:266px;font-size:14px}

/* eso */
.eso{top:1571px;height:376px}
.eso .heading{left:91px;top:42px;color:var(--red);font-size:30px}
.eso .copy{left:91px;width:506px}
.eso .btn{left:91px;top:298px;width:132px;height:40px;background:var(--blue-deep)}
.video-frame{left:626px;top:25px;width:481px;height:299px;background:#f4f4f4;border:1px solid #ccc;box-shadow:0 1px 5px rgba(0,0,0,.2)}
.video-still{left:12px;top:12px;width:457px;height:232px;background:linear-gradient(120deg,#e6e6e6,#bdbdbd 60%,#8c8c8c)}
.video-bar{left:12px;top:244px;width:457px;height:36px;background:#262626}

/* primaria */
.primaria{top:1947px;height:314px;background:var(--blue)}
.primaria .heading{top:60px;color:var(--white)}
.primaria .lead{left:110px;top:118px;width:980px;text-align:center;color:var(--white);font-size:20px;line-height:34px}
.primaria .btn{left:556px;top:218px;width:132px;height:40px;background:#ececec;color:#333;border:1px solid #ccc}

/* infantil */
.infantil{top:2261px;height:444px}
.infantil .photo{left:91px;top:52px;width:492px;height:299px;background:linear-gradient(135deg,#e8e8e8,#c9c9c9 55%,#9a9a9a)}
.infantil .heading{left:606px;top:50px;color:var(--red);font-size:30px}
.infantil .copy{left:606px;width:506px}
.infantil .btn{left:606px;top:303px;width:136px;height:41px;background:var(--teal-dark)}

/* artist */
.artist{top:2705px;height:405px;background:var(--grey-bg)}
.artist .heading{top:44px}
.tile{position:absolute;top:112px;width:249px;height:230px;border-bottom:5px solid var(--red)}
.tile.lead-tile{background:#3a3a3a;border-bottom:none;color:var(--white);text-align:center}
.tile.lead-tile .name{position:absolute;left:0;width:100%;top:140px;font-size:15px;font-weight:500}
.tile.lead-tile .mail{position:absolute;left:0;width:100%;top:164px;font-size:12px}
.tile.lead-tile svg{position:absolute;left:107px;top:96px}

/* footer */
.site-footer{top:3110px;height:221px;background:var(--teal-dark);color:var(--white)}
.foot-brand{left:102px;top:72px;display:flex;align-items:center;gap:10px;font-family:'Oswald',Arial,sans-serif;font-weight:500;font-size:34px;color:var(--white)}
.foot-brand .dot{width:22px;height:22px;border-radius:50%;background:var(--white)}
.foot-title{font-size:14px;text-transform:uppercase;letter-spacing:.4px;top:42px}
.foot-links{left:394px;top:82px;list-style:none;font-size:11px;line-height:25px}
.foot-links li::before{content:"▸ ";font-size:9px}
.touch{left:622px;top:82px;font-size:11px;line-height:20px}
.touch p{margin-bottom:12px}
.form{left:888px;top:80px;width:226px}
.form .row{display:flex;gap:2px;margin-bottom:2px}
.field{height:31px;background:var(--white);color:#555;font-size:11px;display:flex;align-items:center;padding-left:8px;border:1px solid #ddd;flex:1}
.submit{height:36px;margin-top:4px;background:var(--red);display:flex;align-items:center;justify-content:center;font-size:12px;text-transform:uppercase}

.bottom-bar{top:3331px;height:85px;background:var(--bar);color:var(--white)}
.bottom-bar .legal{left:84px;top:36px;font-size:11px}
.socials{left:981px;top:24px;display:flex;gap:18px}
.socials span{width:34px;height:34px;border-radius:50%;border:1.5px solid #ddd}
</style>
</head>
<body>

<header class="site-header">
  <div class="abs phone">
    <svg width="18" height="18" viewBox="0 0 18 18"><rect width="18" height="18" rx="3" fill="#e54430"/><path d="M5 4.5c.5-.5 1.2-.5 1.6 0l1 1.3c.3.4.3 1-.1 1.3l-.6.5c.5 1.1 1.4 2 2.5 2.5l.5-.6c.3-.4.9-.4 1.3-.1l1.3 1c.5.4.5 1.1 0 1.6l-.7.7c-2.8.6-7.8-4.4-7.2-7.2z" fill="#fff"/></svg>
    <span>955 310 4827</span>
  </div>
  <div class="abs brand"><span class="dot"></span>Tovrelly</div>
  <a class="btn quote-btn">Get a Quote</a>
</header>

<nav class="main-nav">
  <ul>
    <li class="active">Welcome</li>
    <li>University and EOI</li>
    <li>ESO &amp; Bachillerato</li>
    <li>Primaria</li>
    <li>Infantíl</li>
    <li>Meet the Artist</li>
    <li>Contact</li>
  </ul>
</nav>

<section class="hero">
  <div class="abs hero-photo" role="img" aria-label="Magician in a black suit and red tie waving a red silk and a wand"></div>
  <svg class="abs play" width="72" height="72" viewBox="0 0 72 72"><circle cx="36" cy="36" r="33" fill="#222" stroke="#eee" stroke-width="3"/><path d="M29 23l20 13-20 13z" fill="#fff"/></svg>
  <h1 class="abs hero-title">Tovrelly Productions</h1>
  <p class="abs hero-sub">Magic shows &amp; Teach English to Spanish kids</p>
  <div class="abs dots"><span class="on"></span><span></span><span></span><span></span></div>
</section>

<section class="welcome">
  <h2 class="abs heading centered">Welcome to <em>Tovrelly</em></h2>
  <p class="abs copy">Lorem Ipsum has been the industry's standard dummy text ever since the 1500s, when an unknown printer took a galley of type and scrambled it to make a type specimen book. It has survived not only five centuries, but also the leap into electronic typesetting, remaining essentially unchanged. It was popularised in the 1960s with the release of Letraset sheets containing Lorem Ipsum passages, and more recently with desktop publishing software like Aldus PageMaker including versions of Lorem Ipsum.</p>
</section>

<section class="university">
  <h2 class="abs heading centered">University <em>and EOI</em></h2>
  <article class="card teal">
    <div class="portrait" role="img" aria-label="Magician juggling in a red tie" style="background:linear-gradient(#f2f2f2,#cfcfcf)"></div>
    <h3>Magic Shows</h3>
    <p>Sleight &amp; Speech is an educational show, directed to English students 12 years or more, combining magic, circus and escapism. A visual, agile and very funny show from the first minute thanks to the interaction between Sam</p>
    <span class="more">Read More »</span>
  </article>
  <article class="card red">
    <div class="portrait" role="img" aria-label="Magician holding a red ball on a dark stage" style="background:linear-gradient(#3a3a3a,#151515)"></div>
    <h3>Teach English to Spanish Kids</h3>
    <p>Sleight &amp; Speech is an educational show, directed to English students 12 years or more, combining magic, circus and escapism. A visual, agile and very funny show from the first minute thanks to the interaction between Sam</p>
    <span class="more">Read More »</span>
  </article>
  <article class="card blue">
    <div class="portrait" role="img" aria-label="Performer balancing a pole mid-act" style="background:linear-gradient(#f4f4f4,#d6d6d6)"></div>
    <h3>Events</h3>
    <p>Sleight &amp; Speech is an educational show, directed to English students 12 years or more, combining magic, circus and escapism. A visual, agile and very funny show from the first minute thanks to the interaction between Sam</p>
    <span class="more">Read More »</span>
  </article>
</section>

<section class="eso">
  <h2 class="abs heading">ESO &amp; Bachillerato</h2>
  <p class="abs copy" style="top:98px">Lorem Ipsum has been the industry's standard dummy text ever since the 1500s, when an unknown printer took a galley of type and scrambled it to make a type specimen book. It has survived not only five centuries, but also the leap into electronic typesetting, remaining essentially unchanged.</p>
  <p class="abs copy" style="top:196px">It was popularised in the 1960s with the release of Letraset sheets containing Lorem Ipsum passages, and more recently with desktop publishing software like Aldus PageMaker including versions of Lorem Ipsum.</p>
  <a class="btn">Read More</a>
  <div class="abs video-frame">
    <div class="abs video-still" role="img" aria-label="Magician in a suit presenting a rubber chicken"></div>
    <svg class="abs" style="left:212px;top:100px" width="56" height="56" viewBox="0 0 56 56"><circle cx="28" cy="28" r="26" fill="#333" fill-opacity=".85"/><path d="M22 17l17 11-17 11z" fill="#fff"/></svg>
    <div class="abs video-bar">
      <svg width="457" height="36" viewBox="0 0 457 36">
        <circle cx="16" cy="18" r="7" fill="none" stroke="#ccc" stroke-width="2"/>
        <path d="M38 14h4l5-4v16l-5-4h-4z" fill="#ccc"/>
        <rect x="52" y="16" width="30" height="4" fill="#e54430"/>
        <rect x="96" y="16" width="210" height="4" fill="#555"/>
        <rect x="96" y="16" width="90" height="4" fill="#e54430"/>
        <text x="318" y="22" fill="#ccc" font-size="11" font-family="Roboto,sans-serif">01:30 / 04:55</text>
        <rect x="408" y="13" width="12" height="10" fill="none" stroke="#ccc" stroke-width="1.5"/>
        <circle cx="438" cy="18" r="5" fill="none" stroke="#ccc" stroke-width="2"/>
      </svg>
    </div>
  </div>
</section>

<section class="primaria">
  <h2 class="abs heading centered">Primaria</h2>
  <p class="abs lead">Lorem Ipsum has been the industry's standard dummy text ever since the 1500s, when an unknown printer took a galley of type and scrambled it to make a type specimen book. It has survived not only five centuries, but also the leap into electronic typesetting, remaining essentially unchanged</p>
  <a class="btn">Read More</a>
</section>

<section class="infantil">
  <div class="abs photo" role="img" aria-label="Smiling performer holding a red ball toward the camera"></div>
  <h2 class="abs heading">Infantíl</h2>
  <p class="abs copy" style="top:96px">Lorem Ipsum has been the industry's standard dummy text ever since the 1500s, when an unknown printer took a galley of type and scrambled it to make a type specimen book. It has survived not only five centuries, but also the leap into electronic typesetting, remaining essentially unchanged.</p>
  <p class="abs copy" style="top:194px">It was popularised in the 1960s with the release of Letraset sheets containing Lorem Ipsum passages, and more recently with desktop publishing software like Aldus PageMaker including versions of Lorem Ipsum.</p>
  <a class="btn">Read More</a>
</section>

<section class="artist">
  <h2 class="abs heading centered">Meet the <em>Artist</em></h2>
  <div class="tile lead-tile" style="left:91px">
    <svg width="36" height="36" viewBox="0 0 36 36"><circle cx="18" cy="18" r="17" fill="#fff" fill-opacity=".2"/><path d="M14 22l8-8M12 18l-2 2a3.5 3.5 0 005 5l2-2M24 18l2-2a3.5 3.5 0 00-5-5l-2 2" stroke="#fff" stroke-width="2.2" fill="none" stroke-linecap="round"/></svg>
    <div class="name">Sam Corwin</div>
    <div class="mail">contact.sam@tovrelly.com</div>
  </div>
  <div class="tile" style="left:348px;background:linear-gradient(#f0f0f0,#cfcfcf)" role="img" aria-label="Team member portrait"></div>
  <div class="tile" style="left:606px;background:linear-gradient(#e8e2dc,#b9aea4)" role="img" aria-label="Team member portrait"></div>
  <div class="tile" style="left:863px;background:linear-gradient(#f2f2f2,#d2cec9)" role="img" aria-label="Team member portrait"></div>
</section>

<footer class="site-footer">
  <div class="abs foot-brand"><span class="dot"></span>Tovrelly</div>
  <h4 class="abs foot-title" style="left:394px">Links</h4>
  <ul class="abs foot-links">
    <li>Customer Support</li>
    <li>Documentation</li>
    <li>Resources</li>
    <li>General FAQs</li>
    <li>Shortcodes</li>
  </ul>
  <h4 class="abs foot-title" style="left:622px">Get in Touch</h4>
  <div class="abs touch">
    <p>Address : 245 Harbor Lane<br>Seacliff CA 90000</p>
    <p>Phone : (555) 014-2290</p>
    <p>Email : info@tovrelly.com</p>
  </div>
  <h4 class="abs foot-title" style="left:888px">Contact Form</h4>
  <div class="abs form">
    <div class="row"><span class="field">Name</span><span class="field">Phone</span></div>
    <div class="row"><span class="field">Email address</span></div>
    <div class="submit">Submit</div>
  </div>
</footer>

<div class="abs bottom-bar" style="position:absolute;left:0;width:1200px">
  <p class="abs legal">Copyright © 2016. All Rights Reserved</p>
  <div class="abs socials"><span></span><span></span><span></span></div>
</div>

</body>
</html>
```